Lark Ridge Property Biz Card
Business card and stationary
Project: Lark Ridge Property Biz Card
Lark Ridge Property Biz Card - Real Estate
Creative Brief
Professional
Dwight Fenmore
DO NOT ADD AN ADDRESS
dfenmore@larkridgeproperty.com
On the front I would like the logo, my name, phone number and email address. Also please have the catch phrase: "We buy houses, any condition! Get Cash Fast! Quick Closing!" The colour scheme of my logo is not set in stone, so please feel free to experiment with the colours.
On the back of the card please have the company logo

```html
<!DOCTYPE html>
<html lang="en">
<head>
<meta charset="utf-8">
<title>Lark Ridge Property – Business Card</title>
<link rel="stylesheet" href="https://fonts.googleapis.com/css2?family=PT+Sans:ital,wght@0,400;0,700;1,700&display=swap">
<style>
  :root {
    --backdrop: #e4e6ea;
    --card-white: #ffffff;
    --brand-blue: #1f3f7a;
    --swoosh-dark: #3a3d42;
    --swoosh-light: #b9bcc1;
    --text-grey: #3c3f45;
  }
  * { margin: 0; padding: 0; box-sizing: border-box; }
  html, body {
    width: 1200px; height: 896px; overflow: hidden;
    background: var(--backdrop);
    font-family: "PT Sans", Arial, sans-serif;
  }
  .canvas {
    width: 1200px; height: 896px;
    display: flex; align-items: center; justify-content: center;
  }
  .card {
    position: relative;
    width: 1000px; height: 572px;
    background: var(--card-white);
    border-radius: 26px;
    overflow: hidden;
    box-shadow: 0 18px 40px rgba(0,0,0,0.18);
  }
  .card-art { position: absolute; inset: 0; width: 100%; height: 100%; }
  .brand {
    position: absolute; left: 48px; top: 44px;
    display: flex; align-items: center; gap: 18px;
  }
  .brand-mark { width: 64px; height: 64px; background: var(--brand-blue); }
  .brand-name {
    font-weight: 700; font-size: 50px; line-height: 1;
    color: var(--brand-blue); text-transform: uppercase;
    letter-spacing: 0.5px;
  }
  .contact {
    position: absolute; left: 250px; top: 210px;
    color: var(--text-grey);
  }
  .person-name {
    font-weight: 400; font-size: 46px; line-height: 1.1;
    color: var(--brand-blue); margin-bottom: 18px;
  }
  .catchphrase {
    font-weight: 700; font-style: italic; font-size: 22px; line-height: 1.25;
    color: var(--brand-blue); margin-bottom: 22px;
  }
  .detail-line {
    display: flex; align-items: center; gap: 10px;
    font-size: 20px; line-height: 1.55;
  }
  .detail-icon { width: 20px; height: 20px; flex: none; }
</style>
</head>
<body>
<main class="canvas">
  <section class="card" aria-label="Lark Ridge Property business card front">
    <svg class="card-art" viewBox="0 0 1000 572" aria-hidden="true">
      <defs>
        <linearGradient id="swooshShade" x1="0" y1="1" x2="1" y2="0">
          <stop offset="0" stop-color="var(--swoosh-light)"/>
          <stop offset="0.45" stop-color="var(--swoosh-dark)"/>
          <stop offset="1" stop-color="var(--swoosh-dark)" stop-opacity="0"/>
        </linearGradient>
      </defs>
      <path class="blue-band" fill="var(--brand-blue)"
            d="M640,0 L1000,0 L1000,572 L600,572 C780,470 830,290 740,150 C710,95 675,45 640,0 Z"/>
      <path class="curve-shadow" fill="url(#swooshShade)"
            d="M430,572 C610,520 720,430 760,300 C770,380 720,480 600,572 Z"/>
    </svg>

    <div class="brand">
      <span class="brand-mark"></span>
      <span class="brand-name">Lark Ridge Property</span>
    </div>

    <div class="contact">
      <h1 class="person-name">Dwight Fenmore</h1>
      <p class="catchphrase">"We buy houses, any condition!<br>Get Cash Fast! Quick Closing!"</p>
      <p class="detail-line">
        <svg class="detail-icon" viewBox="0 0 20 20" aria-label="Phone">
          <circle cx="10" cy="10" r="9" fill="none" stroke="currentColor" stroke-width="1.4"/>
          <path d="M7 5.5 L8.6 5.5 L9.2 8 L8.2 8.8 C8.8 10.2 9.8 11.2 11.2 11.8 L12 10.8 L14.5 11.4 L14.5 13 C11 13.5 6.5 9 7 5.5 Z" fill="currentColor"/>
        </svg>
        <span>: 204-555-0183</span>
      </p>
      <p class="detail-line">
        <svg class="detail-icon" viewBox="0 0 20 20" aria-label="Email">
          <rect x="2" y="4.5" width="16" height="11" fill="none" stroke="currentColor" stroke-width="1.4"/>
          <path d="M2 4.5 L10 11 L18 4.5" fill="none" stroke="currentColor" stroke-width="1.4"/>
        </svg>
        <span>: dfenmore@larkridgeproperty.com</span>
      </p>
    </div>
  </section>
</main>
</body>
</html>
```